Consulting/Brand Licensing business needs business card

We need a business card created for our IP company, that also does consulting and brand licensing. We would like this card to be vague, as our other business' are in the cannabis industry and this is a non-cannabis touching entity. Perhaps something that hints vaguely at the industry without alerting or possibly offending the receiver.

Target Market(s)

CEOs/Key Decision Makers/Industry Leaders

Contact Information for Business Card

No address, simply list Seattle, WA. Phone: 206-555-0147. Name: Dilan Vesterby // email: Dilan@pulvanixa.com

Colors

Designer to choose colors to be used in the design.

Requirements
Must have
• Logo, Name, Email, Phone number, "Consulting, Licensing and Branding Specialists"
Nice to have
• We would like this to be more professional than playful.

```html
<!DOCTYPE html>
<html lang="en">
<head>
<meta charset="utf-8">
<title>Pulvanixa, Inc – Business Card</title>
<link href="https://fonts.googleapis.com/css2?family=Mulish:wght@400;600;700&display=swap" rel="stylesheet">
<style>
  :root {
    --brand-orange: #e04e2c;
    --ink: #1f1f1f;
    --ink-soft: #4a4a4a;
    --rule: #c9c9c9;
    --card: #ffffff;
    --backdrop: #ecebe8;
  }
  * { box-sizing: border-box; margin: 0; padding: 0; }
  html, body {
    width: 1200px;
    height: 960px;
    overflow: hidden;
    background: var(--backdrop);
    font-family: "Mulish", sans-serif;
  }
  .stage { position: relative; width: 1200px; height: 960px; }
  .card {
    position: absolute;
    left: 320px;
    width: 560px;
    height: 320px;
    background: var(--card);
    box-shadow: 0 6px 18px rgba(0,0,0,0.12);
    overflow: hidden;
  }
  .card--front { top: 120px; }
  .card--back  { top: 500px; }

  /* Brand lockup: plain square + company name */
  .lockup {
    display: flex;
    flex-direction: column;
    align-items: center;
  }
  .lockup__mark {
    background: var(--brand-orange);
  }
  .lockup__name {
    color: var(--ink);
    font-weight: 400;
    white-space: nowrap;
  }

  .card--front .front-layout {
    position: absolute;
    inset: 0;
    display: flex;
    flex-direction: column;
    align-items: center;
    justify-content: center;
  }
  .card--front .lockup__mark { width: 78px; height: 78px; }
  .card--front .lockup__name { font-size: 30px; margin-top: 18px; }
  .tagline {
    margin-top: 14px;
    color: var(--ink-soft);
    font-size: 13px;
    letter-spacing: 0.6px;
    text-transform: uppercase;
  }

  .band {
    position: absolute;
    left: 0;
    width: 100%;
    background: var(--brand-orange);
  }
  .band--top { top: 0; height: 12px; }
  .band--bottom { bottom: 22px; height: 14px; }

  .back-layout {
    position: absolute;
    left: 0; right: 0;
    top: 12px;
    bottom: 36px;
    display: flex;
    align-items: center;
  }
  .back-layout .lockup { width: 262px; }
  .back-layout .lockup__mark { width: 62px; height: 62px; }
  .back-layout .lockup__name { font-size: 22px; margin-top: 14px; }

  .divider { width: 1px; height: 160px; background: var(--rule); }
  .contact { padding-left: 26px; }
  .contact__name { color: var(--brand-orange); font-weight: 700; font-size: 17px; }
  .contact__role { color: var(--ink-soft); font-size: 13px; margin-top: 3px; }
  .contact__list { list-style: none; margin-top: 16px; }
  .contact__item {
    display: flex;
    align-items: center;
    gap: 8px;
    color: var(--ink);
    font-size: 14px;
    margin-bottom: 6px;
  }
  .contact__icon { width: 13px; height: 13px; flex: none; }
</style>
</head>
<body>
<main class="stage">

  <section class="card card--front" aria-label="Card front">
    <div class="front-layout">
      <div class="lockup">
        <div class="lockup__mark" role="img" aria-label="Logo placeholder"></div>
        <div class="lockup__name">Pulvanixa, Inc</div>
      </div>
      <p class="tagline">Consulting, Licensing and Branding Specialists</p>
    </div>
  </section>

  <section class="card card--back" aria-label="Card back">
    <div class="band band--top"></div>
    <div class="back-layout">
      <div class="lockup">
        <div class="lockup__mark" role="img" aria-label="Logo placeholder"></div>
        <div class="lockup__name">Pulvanixa, Inc</div>
      </div>
      <div class="divider"></div>
      <div class="contact">
        <p class="contact__name">Dilan Vesterby</p>
        <p class="contact__role">President</p>
        <ul class="contact__list">
          <li class="contact__item">
            <svg class="contact__icon" viewBox="0 0 16 16" aria-hidden="true">
              <path fill="#e04e2c" d="M3.6 1.2l2.3 2.6-1.3 1.8c.9 2 2.6 3.7 4.6 4.6l1.8-1.3 2.6 2.3-1.4 2.3C7.3 13.4 2.6 8.7 1.3 3.5z"/>
            </svg>
            <span>206-555-0147</span>
          </li>
          <li class="contact__item">
            <svg class="contact__icon" viewBox="0 0 16 16" aria-hidden="true">
              <rect x="1" y="3.5" width="14" height="10" rx="1" fill="#e04e2c"/>
              <path d="M1.8 4.3L8 9l6.2-4.7" fill="none" stroke="#ffffff" stroke-width="1.3"/>
            </svg>
            <span>Dilan@pulvanixa.com</span>
          </li>
          <li class="contact__item">
            <svg class="contact__icon" viewBox="0 0 16 16" aria-hidden="true">
              <path fill="#e04e2c" d="M8 1a5 5 0 0 0-5 5c0 3.8 5 9 5 9s5-5.2 5-9a5 5 0 0 0-5-5z"/>
              <circle cx="8" cy="6" r="1.8" fill="#ffffff"/>
            </svg>
            <span>Seattle, WA</span>
          </li>
        </ul>
      </div>
    </div>
    <div class="band band--bottom"></div>
  </section>

</main>
</body>
</html>
```